Tellwick Asset Management - Corporate Letter Head Project

Looking for a classy design based on our current logo. Please find current logo source file in files. With our color scheme.

Target Market(s)

We're an investment firm, the letterhead needs to look professional and attractive to clients.

Industry/Entity Type

Hedgefund

Colors
0054AA
0677BA
7BADD7
CADEEF
E8F1F8

Requirements
Must have
• Our logo, address, phone number, and email

```html
<!DOCTYPE html>
<html lang="en">
<head>
<meta charset="utf-8">
<title>Tellwick Asset Management – Letterhead</title>
<link rel="stylesheet" href="https://fonts.googleapis.com/css2?family=Cinzel:wght@400;500&family=Work+Sans:wght@400;600&display=swap">
<style>
  :root {
    --navy: #0b1652;
    --text-grey: #5a5a5a;
    --rule-grey: #555555;
    --paper: #ffffff;
  }
  * { margin: 0; padding: 0; box-sizing: border-box; }
  html, body { width: 848px; height: 1200px; overflow: hidden; background: var(--paper); }
  .letterhead {
    position: relative;
    width: 848px;
    height: 1200px;
    border: 1px solid var(--navy);
    background: var(--paper);
    font-family: "Work Sans", Arial, sans-serif;
    color: var(--text-grey);
  }
  .brand {
    position: absolute;
    left: 514px;
    top: 94px;
    display: flex;
    align-items: center;
    gap: 9px;
  }
  .brand-square {
    width: 44px;
    height: 46px;
    border: 1px solid var(--navy);
  }
  .brand-name {
    font-family: "Cinzel", Georgia, serif;
    font-weight: 500;
    color: var(--navy);
    font-size: 17px;
    line-height: 20px;
    letter-spacing: 0.5px;
  }
  .content {
    position: absolute;
    left: 121px;
    width: 604px;
  }
  .heading {
    font-family: "Cinzel", Georgia, serif;
    font-weight: 400;
    color: var(--navy);
    letter-spacing: 1.5px;
  }
  .heading-main { top: 266px; font-size: 29px; line-height: 34px; }
  .heading-sub { top: 656px; font-size: 27px; line-height: 31px; word-spacing: 6px; }
  .body-copy {
    font-size: 12.6px;
    line-height: 18.5px;
    text-align: justify;
  }
  .body-copy p + p { margin-top: 18.5px; }
  .copy-one { top: 316px; }
  .copy-two { top: 737px; }
  .footer-rule {
    position: absolute;
    left: 121px;
    top: 1113px;
    width: 604px;
    height: 8px;
  }
  .footer-contact {
    position: absolute;
    left: 118px;
    top: 1130px;
    width: 612px;
    font-size: 10.6px;
    letter-spacing: 1px;
    color: var(--rule-grey);
    white-space: nowrap;
    text-align: center;
  }
  .footer-contact strong { font-weight: 600; }
  .footer-contact .sep { margin: 0 7px; }
</style>
</head>
<body>
<main class="letterhead">
  <header class="brand">
    <span class="brand-square"></span>
    <span class="brand-name">Tellwick Asset<br>Management</span>
  </header>

  <h1 class="content heading heading-main">Headline</h1>

  <section class="content body-copy copy-one">
    <p>Quia sit, quaessit, aut maximolores invello eveliam quatempe mod mos essumqu aessimagnam et percia quiaspitiis dia verumque volupit utatum quidersperis et optatesequi rehenis a nobis di ut veliamusam et, quis sam atem hit di nossit dolupta conse adit ut voluptatur, totaquid quodipsum dit, veles exceatiates et odiorepel est et volorer cimiliquam voluptae ra eost voluptatur ressimagnit quo comnimo luptur, velenda dem re, tem as consed magnis repeles et et ut enihilita sunti dem explique vollandebit, omniscient ut in rest lab ilis quis voluptatur, sum et exerem sitaspi cienimus num expeles citinitae nulluptassed elitas alit ommolorrum doluptation poresto ritaturion re voluptat veligenda eatempo reptae re preperrum ipsanis molorios modite dellit, soluptaspiti cum remque conse cus doloribea dolupta tecatur modia que perio blaboritat verum a volore magnis que nullanda volupta cum dis milia quia nos eosapellam corem eratur, suntus di quiscienecea culpa quam eumquam, aliquam rehendebit, sedis dolumqui atiossit doluptatur? Ibusape ribusdam venecernatis coriate mporem reius ea id ut quo incti opti aut unt voluptae pel incteseque net voluptis modis que non reici to tet, sedi con nam ipitiorum hit a nonsecae vel iderio. Cus denimus, ut dolenda sit quunt minum eate plaut vel magnam endaeca borumqui omnihilic tendisq uature etusandit que volorrum explique et maio et landi corem. Litatur, sundicate ommod esed quo etusdae dolor autem faci quam lam aut fugit excearc hitatur, comnimus accus nobis asit volores exero core eat assitii scidia qui ipsumquaest facitiustem alis earis del inis plam apiciumque sitatiusa suntur?</p>
  </section>

  <h2 class="content heading heading-sub">Lupta nest, sum nam aut occae pera aperend itest</h2>

  <section class="content body-copy copy-two">
    <p>Ga. Aligentibus sunt a simet hiciati occuptat quodis dolut iur, apiendigname videbis pa ipsaeri busdaes volupti bearchicatis magnist vere, sumquo bearci veliquatiore ommodis cimenis eosapis vitio beatqua mendunt mi, con rerspis atianim illestis dolorese res dolorpor reptaspiti ut eos iunt labo. Uciis perspel lorepudipid mint fuga. Ut in conse dolor aut volo vella volorit iorpore stibustore plis aut haria ant derruptae elisi iliciame nonsecus ut officimpore soluptatio is dest, eveniasit id maione cum rehento tatiur as eveniet ea voluptias quae non repra que nusciam sapienis atet hil illat.</p>
    <p>Es dolupis volestiataes nonsecus modis deles namus santem vellatur, omniene molores ulparum quis volor alibus debis dolore natur sunt erernam quid mi, verfersperis que</p>
    <p>Torem reptissi quis quid ut ea consendebis molorerite pore sequamusdae velligniam rest, offici nis ipsam ium quati dici officid quo tetur resed quistisquiae nonsequiae repe sandaep errorrore et re officit erchitatis eum fugit, eium volorecessi blandam usapienducit iduciam fuga. Ut prem consent quiani intem iur sunt qui consecume quo deleniaernam nimi, te dolorionet ma quatur mo occum id exceprem faciantem haruptatiam ne laces es perum, eaqui delibus, ium earcillati untorum, nes eum ipsa conemporerum issi non nienit erundaepelit rae omnis aut laccul luptis eos arite sum ium et explicte venimet incto moloraes etur aruptat ionsequis mos erchicil et labor seque volest maiosam, a perovid estiatem ea velit autemporit explicia nesti aces dolo int ut. a perovid estiatem ea velit autemporit explicia nesti aces dolo int ut.</p>
  </section>

  <footer>
    <svg class="footer-rule" viewBox="0 0 604 8" aria-hidden="true">
      <line x1="4" y1="4" x2="600" y2="4" stroke="#555555" stroke-width="1"/>
      <circle cx="4" cy="4" r="2.6" fill="#555555"/>
      <circle cx="600" cy="4" r="2.6" fill="#555555"/>
    </svg>
    <p class="footer-contact">Streetname zip code<span class="sep">/</span><strong>phone:</strong> 012 345678<span class="sep">/</span><strong>Email:</strong> pr@tellwickassetmgt.com<span class="sep">/</span><strong>www.tellwickassetmgt.com</strong></p>
  </footer>
</main>
</body>
</html>
```